Trade Show Booth Design for Saas company

Brightpost Suite is a startup company that will be launching its software as a service product at a trade show in the near future. We are looking for something that really pops and is appealing to the eye. Attached is the branding guidelines along with the color palette. The pink should be predominant. We’re not so concerned with the copy of your design for the contest, but rather the design itself. We can work on the copy later. You can utilize any copy or graphics from our website at www.brightpostsuite.example. You can also learn more about us at the website. One element from the website that is worth mentioning, and optional, is the hub and spoke graphic in the “Connect All Your SMTP Email Service Providers” section. (It is attached.) We will provide high resolution versions of anything you need. The display will be a flat 10 foot wide by 8 foot tall, one piece of fabric. We will also need the graphics for the 39in x 19in x 12in Counter Graphic Print, but probably just the logo on it. We are open to design elements that include the use of a person or not. We basically want something modern and very eye-catching.
Potential headline and text:
One place to manage it all
Guided by expert mailers, Brightpost Suite combines every aspect of email marketing into a powerful package.

```html
<!DOCTYPE html>
<html lang="en">
<head>
<meta charset="utf-8">
<title>Brightpost Suite – Trade Show Backdrop</title>
<link href="https://fonts.googleapis.com/css2?family=Poppins:wght@400;500;600;700;800&display=swap" rel="stylesheet">
<style>
  :root {
    --pink: #f0147f;
    --navy: #1c1a45;
    --white: #ffffff;
    --stage: #e9e9ea;
    --card-shade: #ececef;
    --illo-blue: #6f7cf2;
    --illo-violet: #a770f0;
    --illo-cyan: #36c9f0;
  }
  * { box-sizing: border-box; margin: 0; padding: 0; }
  html, body { width: 1200px; height: 2222px; overflow: hidden; }
  body {
    background: var(--stage);
    font-family: "Poppins", sans-serif;
    color: var(--navy);
    position: relative;
  }
  .backdrop {
    position: absolute;
    left: 50px; top: 561px;
    width: 1100px; height: 1100px;
    background: var(--white);
    box-shadow: 0 18px 40px rgba(0,0,0,0.18);
  }
  .brand {
    position: absolute; left: 68px; top: 110px;
    display: flex; align-items: center; gap: 22px;
  }
  .brand-square { width: 74px; height: 74px; background: var(--pink); }
  .brand-name {
    font-weight: 600; font-size: 46px; color: var(--navy); letter-spacing: -0.5px;
  }
  .headline {
    position: absolute; left: 64px; top: 248px;
    font-weight: 800; font-size: 78px; line-height: 66px;
    letter-spacing: -1px; text-transform: uppercase; color: var(--navy);
  }
  .headline .accent { color: var(--pink); }
  .intro {
    position: absolute; left: 66px; top: 466px; width: 500px;
    font-weight: 500; font-size: 20px; line-height: 23px; color: var(--navy);
  }
  .hero-illustration {
    position: absolute; left: 573px; top: 88px;
    width: 478px; height: 438px; border-radius: 24px;
    background: linear-gradient(150deg, var(--illo-violet), var(--illo-blue) 55%, var(--illo-cyan));
    opacity: 0.85;
  }
  .features {
    position: absolute; left: 66px; top: 577px;
    width: 968px; height: 385px;
    background: var(--navy); border-radius: 20px; overflow: hidden;
  }
  .features .corner { position: absolute; background: var(--pink); }
  .corner-tl-h { left: 0; top: 0; width: 152px; height: 30px; border-top-left-radius: 20px; }
  .corner-tl-v { left: 0; top: 0; width: 36px; height: 145px; border-top-left-radius: 20px; }
  .corner-br-h { right: 0; bottom: 0; width: 146px; height: 30px; border-bottom-right-radius: 20px; }
  .corner-br-v { right: 0; bottom: 0; width: 26px; height: 144px; border-bottom-right-radius: 20px; }
  .feature-card {
    position: absolute; top: 52px; width: 210px; height: 279px;
    background: var(--white); border-radius: 10px; overflow: hidden;
    text-align: center; padding: 14px 12px 0;
  }
  .feature-card::before, .feature-card::after {
    content: ""; position: absolute; border-radius: 50%; background: var(--card-shade);
  }
  .feature-card::before { width: 90px; height: 90px; left: -40px; top: -40px; }
  .feature-card::after { width: 110px; height: 110px; right: -50px; bottom: -55px; }
  .card-1 { left: 50px; } .card-2 { left: 271px; } .card-3 { left: 492px; } .card-4 { left: 713px; }
  .feature-icon {
    position: relative; z-index: 1;
    width: 73px; height: 73px; margin: 0 auto 12px;
    border-radius: 50%; background: var(--pink);
    border: 3px solid var(--navy);
    display: flex; align-items: center; justify-content: center;
  }
  .feature-title {
    position: relative; z-index: 1;
    font-weight: 700; font-size: 17px; line-height: 20px;
    text-transform: uppercase; color: var(--navy);
  }
  .feature-text {
    position: relative; z-index: 1;
    font-weight: 400; font-size: 16px; line-height: 19px; color: var(--navy);
  }
  .website {
    position: absolute; left: 0; width: 100%; top: 992px;
    text-align: center; font-weight: 700; font-size: 34px; letter-spacing: 3px;
    color: var(--navy);
  }
  .website .accent { color: var(--pink); }
</style>
</head>
<body>
  <main class="backdrop">
    <div class="brand">
      <span class="brand-square"></span>
      <span class="brand-name">Brightpost Suite</span>
    </div>

    <h1 class="headline">One Place<br><span class="accent">To Manage</span><br>It All</h1>
    <p class="intro">Guided by expert mailers, Brightpost Suite combines every aspect of email marketing into a powerful package</p>

    <div class="hero-illustration" role="img" aria-label="Illustration of two people working with a large email analytics dashboard"></div>

    <section class="features">
      <span class="corner corner-tl-h"></span>
      <span class="corner corner-tl-v"></span>
      <span class="corner corner-br-h"></span>
      <span class="corner corner-br-v"></span>

      <article class="feature-card card-1">
        <div class="feature-icon">
          <svg width="38" height="38" viewBox="0 0 24 24" fill="#fff"><path d="M20 3c-4 0-8 2-10.5 6L6 9.5 3.5 13l4 1 3.5 3.5 1 4 3.5-2.5.5-3.5c4-2.5 6-6.5 6-10.5V3h-2zm-4 6a2 2 0 1 1 0-.01z"/><path d="M5 16l-2 5 5-2z"/></svg>
        </div>
        <h2 class="feature-title">Effortless Onboarding</h2>
        <p class="feature-text">We'll get you sending emails in no time.</p>
      </article>

      <article class="feature-card card-2">
        <div class="feature-icon">
          <svg width="40" height="40" viewBox="0 0 24 24"><g fill="#fff"><circle cx="12" cy="12" r="7"/><rect x="10.3" y="2" width="3.4" height="5" rx="1"/><rect x="10.3" y="17" width="3.4" height="5" rx="1"/><rect x="2" y="10.3" width="5" height="3.4" rx="1"/><rect x="17" y="10.3" width="5" height="3.4" rx="1"/><rect x="10.3" y="2" width="3.4" height="5" rx="1" transform="rotate(45 12 12)"/><rect x="10.3" y="17" width="3.4" height="5" rx="1" transform="rotate(45 12 12)"/><rect x="2" y="10.3" width="5" height="3.4" rx="1" transform="rotate(45 12 12)"/><rect x="17" y="10.3" width="5" height="3.4" rx="1" transform="rotate(45 12 12)"/></g><circle cx="12" cy="12" r="3" fill="#f0147f"/></svg>
        </div>
        <h2 class="feature-title">Scalable Infrastructure</h2>
        <p class="feature-text">Start slow and build your monthly email volume in the millions.</p>
      </article>

      <article class="feature-card card-3">
        <div class="feature-icon">
          <svg width="40" height="40" viewBox="0 0 24 24" fill="none" stroke="#fff" stroke-width="1.6"><circle cx="12" cy="12" r="6.5"/><ellipse cx="12" cy="12" rx="3" ry="6.5"/><path d="M5.5 12h13M6.5 9h11M6.5 15h11"/><path d="M12 2v2M12 20v2M2 12h2M20 12h2M4.9 4.9l1.4 1.4M17.7 17.7l1.4 1.4M4.9 19.1l1.4-1.4M17.7 6.3l1.4-1.4" stroke-width="2"/></svg>
        </div>
        <h2 class="feature-title">The Right Messages to the Right People</h2>
        <p class="feature-text">Use data and insights to segment your list and personalize your emails.</p>
      </article>

      <article class="feature-card card-4">
        <div class="feature-icon">
          <svg width="40" height="40" viewBox="0 0 24 24" fill="none" stroke="#fff" stroke-width="1.8"><path d="M4 20h16"/><path d="M7 19v-5M11 19v-7M15 19v-4M19 19v-8" stroke-width="2.6"/><path d="M4 12l5-4 3 2 6-6M15 4h3v3"/></svg>
        </div>
        <h2 class="feature-title">Significant ROI</h2>
        <p class="feature-text">For every $1 you spend on email marketing, you can expect an average return of $40 (Mailmetric, 2022).</p>
      </article>
    </section>

    <p class="website">www.<span class="accent">brightpostsuite</span>.example</p>
  </main>
</body>
</html>
```